Concrete Finishing business needs new business card and a logo design

We are a family owned and operated, concrete finishing business. 2020 marks our 33 rd year in business. We operate under Harold P. Mercer and Sons Concrete Contractors Ltd. Harold P was my father and founder of the company. We usually shorten the name and use H P Mercer & Sons Ltd. Most people in the Concrete Finishing industry tend to know us by our last name 'Mercer' . in honour of our father, we would still like to have his name on the cards and logo but are open to shortening it to H.P (maybe in a small font with the H on top of the P ) and focusing more on the "Mercer & Sons."....Or maybe something with just the initials HPM...or if you could use the "P" and somehow incorporate an artistic drawing/shape of a 'power trowel' (what we use apply a smooth finish to the concrete with) but still visually see that its a P, would be cool. Would like to see designs using Black with silver or grey lettering but are open to other ideas. Seen a business card online with the front of the business card looking like concrete and with just the word CONCRETE on it... On the back was the company name , address and contact info of the company....looked really good! i clicked doubled sided in case of something like that but we are open to just single sided as well. After viewing some of the designs, maybe a pop of colour would be nice ... open to any ideas and colours.😊

Target Market(s)

Construction

```html
<!DOCTYPE html>
<html lang="en">
<head>
<meta charset="utf-8">
<title>H P Mercer &amp; Sons Ltd. — Business Card</title>
<link rel="stylesheet" href="https://fonts.googleapis.com/css2?family=Michroma&family=Oswald:wght@500&family=Montserrat:wght@400&display=swap">
<style>
  :root {
    --stage: #0c0c0c;
    --card-dark: #161616;
    --card-light: #262626;
    --silver: #b9b9b9;
    --silver-dim: #8d8d8d;
    --rule: #9a9a9a;
  }
  * { box-sizing: border-box; margin: 0; padding: 0; }
  html, body {
    width: 1200px;
    height: 900px;
    overflow: hidden;
    background: var(--stage);
  }
  .stage {
    position: relative;
    width: 1200px;
    height: 900px;
    background: radial-gradient(ellipse at 60% 40%, #1c1c1c 0%, var(--stage) 70%);
  }
  .card {
    position: absolute;
    left: 240px;
    width: 720px;
    height: 390px;
    background: linear-gradient(135deg, var(--card-dark) 0%, #1d1d1d 55%, var(--card-light) 100%);
    box-shadow: 0 18px 40px rgba(0, 0, 0, 0.7);
  }
  .card--front { top: 45px; }
  .card--back { top: 465px; }

  /* Front */
  .brand {
    position: absolute;
    left: 0;
    right: 0;
    top: 118px;
    text-align: center;
    font-family: "Michroma", sans-serif;
    color: var(--silver);
  }
  .brand__initials {
    font-size: 72px;
    line-height: 1;
    letter-spacing: -2px;
  }
  .brand__name {
    margin-top: 14px;
    font-size: 21px;
    letter-spacing: 1px;
  }

  /* Back */
  .holder {
    position: absolute;
    right: 398px;
    top: 150px;
    text-align: right;
  }
  .holder__name {
    font-family: "Oswald", sans-serif;
    font-weight: 500;
    font-size: 48px;
    line-height: 1;
    letter-spacing: 1px;
    color: var(--silver-dim);
    text-transform: uppercase;
    transform: scaleX(0.85);
    transform-origin: right center;
  }
  .holder__role {
    margin-top: 8px;
    font-family: "Montserrat", sans-serif;
    font-size: 18px;
    color: var(--silver-dim);
  }
  .divider {
    position: absolute;
    left: 345px;
    top: 110px;
    width: 2px;
    height: 160px;
    background: var(--rule);
  }
  .contact {
    position: absolute;
    left: 372px;
    top: 112px;
    font-family: "Montserrat", sans-serif;
    font-size: 17px;
    line-height: 25px;
    color: #d2d2d2;
    list-style: none;
  }
  .contact__address { margin-bottom: 6px; }
  .contact__line {
    display: flex;
    align-items: center;
    gap: 9px;
  }
  .contact__icon {
    width: 14px;
    height: 14px;
    flex: none;
    fill: none;
    stroke: #d2d2d2;
    stroke-width: 1.4;
  }
</style>
</head>
<body>
<main class="stage">

  <section class="card card--front" aria-label="Card front">
    <div class="brand">
      <div class="brand__initials">HPM</div>
      <div class="brand__name">H P MERCER &amp; SONS LTD.</div>
    </div>
  </section>

  <section class="card card--back" aria-label="Card back">
    <div class="holder">
      <div class="holder__name">Derek Mercer</div>
      <div class="holder__role">Founder</div>
    </div>
    <div class="divider"></div>
    <ul class="contact">
      <li class="contact__address">P.O.Box 41, Site 8, RR#2<br>Harbour Point, NL A0K 2B0</li>
      <li class="contact__line">
        <svg class="contact__icon" viewBox="0 0 14 14" aria-hidden="true"><path d="M3 1.5 L5 4.5 L4 6 C5 8 6 9 8 10 L9.5 9 L12.5 11 L11 13 C6 12.5 1.5 8 1 3 Z"/></svg>
        (555) 214-3722
      </li>
      <li class="contact__line">
        <svg class="contact__icon" viewBox="0 0 14 14" aria-hidden="true"><rect x="3.5" y="1.5" width="7" height="4"/><rect x="1.5" y="5.5" width="11" height="5"/><rect x="3.5" y="9" width="7" height="3.5"/></svg>
        (555) 214-3217
      </li>
      <li class="contact__line">
        <svg class="contact__icon" viewBox="0 0 14 14" aria-hidden="true"><rect x="3.5" y="1" width="7" height="12" rx="1"/><line x1="6" y1="11" x2="8" y2="11"/></svg>
        (555) 214-3294 Dale-Res
      </li>
      <li class="contact__line">
        <svg class="contact__icon" viewBox="0 0 14 14" aria-hidden="true"><rect x="1.5" y="3" width="11" height="8"/><path d="M1.5 3 L7 7.5 L12.5 3"/></svg>
        hp_mercer@mailbox.ca
      </li>
    </ul>
  </section>

</main>
</body>
</html>
```